Web page design for food business

The website is pantryloop.com.au and is an ordering website with thumbnails for purchasing high quality delicatessen products + fruit & vegetables.
The site is simple with a focus on clicking foods to buy and then pay for. There are no complicated product reviews or anything. Aside from the normal about us and contact us pages the website is essentially thumbnails for ordering and a high quality homepage to educate and showcase the business when people go to the URL.
There are 2 main tasks
The first task is a page design (i.e. header, footer, sides...) to carry through for all the pages in the website.
The second task is for the homepage specifically. I want a professional looking homepage with 3 large slide banners that look "elegant" and "artisan" as this is a deli website not a general grocery website. One slider should refer to "daily deliveries" and I will leave the other 2 sliders to your professional judgement. The homepage should also provide for room under the slide banner for specials/products of the month/etc and general promotional information
Target Market(s)
higher income earners, foodies, professionals, quality foods
Industry/Entity Type
Food Store
Number of Pages Required
2 page
Requirements
Must have
- Fresh quality food ready to be delivered
- Ease of ordering
- The feel of a high quality deli
Nice to have
- References to fresh fruit and vegetables for greenery and freshness
Should not have
- .

```html
<!DOCTYPE html>
<html lang="en">
<head>
<meta charset="utf-8">
<title>pantryloop.com.au — Fresh Food Delivery</title>
<link href="https://fonts.googleapis.com/css2?family=Open+Sans:wght@400;600;700;800&display=swap" rel="stylesheet">
<style>
:root{
  --orange:#f47b20;
  --orange-dark:#d9631a;
  --orange-light:#fbb079;
  --charcoal:#2f2f2f;
  --footer:#2a2a2a;
  --footer-deep:#1c1c1c;
  --text:#444;
  --muted:#999;
  --line:#e2e2e2;
  --page:#ffffff;
  --soft:#f4f4f4;
  --green:#3f8f2a;
  --lime:#c8e03a;
}
*{box-sizing:border-box;margin:0;padding:0}
html,body{width:727px;height:1200px;overflow:hidden}
body{font-family:"Open Sans",Arial,sans-serif;color:var(--text);background:var(--page);font-size:8px;position:relative}
.wrap{width:687px;margin:0 auto}

/* top bar */
.topbar{height:18px;background:var(--soft);border-bottom:1px solid var(--line)}
.topbar .wrap{display:flex;justify-content:space-between;align-items:center;height:18px;font-size:6.5px;color:var(--muted)}
.topbar nav{display:flex;gap:14px}

/* header */
.header .wrap{height:58px;display:flex;align-items:center;justify-content:space-between}
.brand{display:flex;flex-direction:column}
.brand-name{font-size:17px;font-weight:700;color:var(--charcoal);letter-spacing:-.3px}
.brand-tag{font-size:6.5px;color:var(--muted);margin-top:1px}
.search{display:flex;width:190px;height:18px}
.search span{flex:1;border:1px solid var(--line);font-size:6.5px;color:#aaa;padding:4px 6px}
.search b{width:48px;background:var(--orange);color:#fff;font-size:6.5px;display:flex;align-items:center;justify-content:center;gap:3px}
.contact{display:flex;align-items:center;gap:6px}
.contact .ring{width:20px;height:20px;border-radius:50%;background:var(--orange);display:flex;align-items:center;justify-content:center}
.contact small{font-size:6px;color:var(--muted);display:block}
.contact strong{font-size:11px;color:var(--orange);font-weight:700}

/* nav */
.mainnav{background:var(--charcoal);height:24px}
.mainnav .wrap{display:flex;justify-content:space-between;height:24px;align-items:center}
.mainnav ul{list-style:none;display:flex}
.mainnav li{color:#fff;font-size:7.5px;font-weight:700;padding:0 14px;line-height:24px}
.mainnav li.active{background:var(--orange)}
.allproducts{background:var(--orange);color:#fff;font-size:7.5px;font-weight:700;height:24px;line-height:24px;padding:0 14px;display:flex;gap:10px}

/* layout */
.content{display:flex;gap:12px;padding-top:8px}
.sidebar{width:165px}
.main{width:510px}

.panel{border:1px solid var(--line);margin-bottom:12px}
.panel h3{background:var(--orange);color:#fff;font-size:8px;font-weight:700;padding:6px 9px}
.panel ul{list-style:none;padding:6px 9px}
.panel li{font-size:6.8px;line-height:16px;border-bottom:1px dotted var(--line);color:#666}
.panel li::before{content:"›";color:var(--orange);margin-right:5px;font-weight:700}
.panel li:last-child{border:0}

.promo{height:310px;margin-bottom:14px;display:flex;flex-direction:column}
.promo-photo{height:165px;background:linear-gradient(160deg,#6b8f3a,#a6b84c 40%,#c7463a 75%,#5c7d2e)}
.promo-copy{flex:1;background:var(--green);color:#fff;padding:14px 12px}
.promo-copy .fresh{font-size:26px;font-weight:800;line-height:1}
.promo-copy .quality{font-size:12px;font-weight:700;margin-left:4px}
.promo-copy .ready{font-size:11px;font-weight:700;margin-top:2px}
.promo-copy .delivered{font-size:24px;font-weight:800;color:var(--lime);line-height:1.1}
.promo-copy p{font-size:6.3px;line-height:9px;margin-top:8px;opacity:.9}

.newsletter{border:1px solid var(--line);padding:10px}
.newsletter h4{font-size:8.5px;font-weight:700;color:var(--charcoal)}
.newsletter p{font-size:6.3px;color:var(--muted);margin:5px 0 8px;line-height:9px}
.newsletter .field{border:1px solid var(--line);font-size:6.5px;color:#aaa;padding:5px 6px;margin-bottom:6px}
.newsletter .btn{background:var(--orange);color:#fff;font-size:7px;font-weight:700;text-align:center;padding:5px 0}

/* hero */
.hero{height:230px;position:relative;background:linear-gradient(100deg,var(--orange-dark),var(--orange) 45%,var(--orange-light));overflow:hidden}
.hero-photo{position:absolute;right:0;top:0;width:260px;height:230px;background:linear-gradient(120deg,rgba(255,255,255,0) 0%,#e8d2bd 30%,#c9a888 55%,#6f9a3e 80%,#9fbf5a)}
.hero-copy{position:absolute;left:24px;top:44px;color:#fff;width:220px}
.hero-copy h1{font-size:30px;font-weight:800;line-height:31px;letter-spacing:.5px}
.hero-copy p{font-size:7.5px;line-height:11px;margin:8px 0 14px}
.hero-copy .btn{display:inline-block;background:var(--charcoal);font-size:8px;font-weight:700;padding:7px 16px}

.features{display:flex;gap:8px;margin-top:12px}
.feature{flex:1;height:60px;background:var(--orange);color:#fff;display:flex;align-items:center;gap:8px;padding:0 8px}
.feature .icon{width:36px;height:36px;background:var(--orange-dark);display:flex;align-items:center;justify-content:center;flex-shrink:0}
.feature h5{font-size:8px;font-weight:700}
.feature p{font-size:6.2px;line-height:8.5px;margin-top:2px;opacity:.92}

.section-title{font-size:9px;font-weight:800;color:var(--charcoal);margin:15px 0 8px;padding-bottom:5px;border-bottom:1px solid var(--line)}
.grid{display:grid;grid-template-columns:repeat(4,120px);gap:10px}
.card{border:1px solid var(--line);height:140px;padding:6px;display:flex;flex-direction:column}
.card .thumb{height:76px;margin:0 8px}
.card h6{font-size:7px;font-weight:700;color:var(--orange);margin-top:6px}
.card .price{font-size:7.5px;font-weight:700;color:var(--charcoal);margin-top:2px}
.card .price s{color:var(--muted);font-weight:400;margin-right:4px}
.card .buy{display:flex;gap:4px;margin-top:auto}
.card .qty{width:26px;border:1px solid var(--line);font-size:6px;text-align:center;padding:3px 0;color:#888}
.card .btn{flex:1;background:var(--orange);color:#fff;font-size:6.5px;font-weight:700;text-align:center;padding:3px 0}

.banana{background:radial-gradient(ellipse at 50% 55%,#f3d23a 0 45%,#fff 60%)}
.onion{background:radial-gradient(circle at 50% 55%,#c99a62 0 40%,#fff 55%)}
.chilli{background:radial-gradient(ellipse at 50% 50%,#d3281c 0 30%,#fff 50%)}
.berry{background:radial-gradient(circle at 50% 55%,#d8322f 0 42%,#fff 58%)}
.orange{background:radial-gradient(circle at 50% 50%,#f58a1c 0 42%,#fff 55%)}
.tomato{background:radial-gradient(circle at 50% 55%,#cf2e24 0 42%,#fff 56%)}
.cabbage{background:radial-gradient(circle at 50% 55%,#7fb040 0 44%,#fff 58%)}
.fig{background:radial-gradient(circle at 50% 55%,#5a2f3f 0 40%,#fff 55%)}
.cherry{background:radial-gradient(circle at 50% 60%,#8e1424 0 38%,#fff 54%)}
.pomegranate{background:radial-gradient(circle at 50% 55%,#b51f2c 0 42%,#fff 56%)}
.redonion{background:radial-gradient(circle at 50% 55%,#6e2a5a 0 40%,#fff 55%)}
.garlic{background:radial-gradient(circle at 50% 55%,#e6dcc7 0 42%,#fff 56%)}

/* footer */
.footer{position:absolute;left:0;top:1000px;width:727px;height:200px;background:var(--footer);color:#bbb}
.footer .wrap{display:flex;gap:14px;padding-top:20px}
.footer .col{flex:1}
.footer h6{color:#fff;font-size:7.5px;font-weight:700;margin-bottom:8px}
.footer li{list-style:none;font-size:6.3px;line-height:12px}
.social li{display:flex;align-items:center;gap:5px;line-height:16px}
.social i{width:12px;height:12px;border-radius:50%;background:#555;display:inline-block}
.copyright{position:absolute;bottom:0;left:0;right:0;height:22px;background:var(--footer-deep);font-size:6.3px;color:#888;text-align:center;line-height:22px}
</style>
</head>
<body>

<div class="topbar">
  <div class="wrap">
    <span>Welcome to pantryloop.com.au</span>
    <nav><span>My Account</span><span>Wish List</span><span>Login</span><span>Register</span><span>Your Cart: 0 items</span></nav>
  </div>
</div>

<header class="header">
  <div class="wrap">
    <div class="brand">
      <span class="brand-name">pantryloop.com.au</span>
      <span class="brand-tag">Fresh Food Delivery</span>
    </div>
    <div class="search"><span>Enter your search</span><b>
      <svg width="7" height="7" viewBox="0 0 10 10"><circle cx="4" cy="4" r="3" fill="none" stroke="#fff" stroke-width="1.5"/><path d="M6.5 6.5L9 9" stroke="#fff" stroke-width="1.5"/></svg>SEARCH</b></div>
    <div class="contact">
      <span class="ring"><svg width="10" height="10" viewBox="0 0 24 24"><path fill="#fff" d="M6.6 10.8a15 15 0 006.6 6.6l2.2-2.2a1 1 0 011-.25 11.4 11.4 0 003.6.57 1 1 0 011 1V20a1 1 0 01-1 1A17 17 0 013 4a1 1 0 011-1h3.5a1 1 0 011 1c0 1.25.2 2.45.57 3.57a1 1 0 01-.25 1z"/></svg></span>
      <div><small>Call us</small><strong>1800 555 019</strong></div>
    </div>
  </div>
</header>

<div class="mainnav">
  <div class="wrap">
    <ul><li class="active">HOME</li><li>SPECIALS ▾</li><li>DELIVERY</li><li>CONTACT US</li></ul>
    <div class="allproducts"><span>ALL PRODUCTS</span><span>☰</span></div>
  </div>
</div>

<div class="wrap content">
  <aside class="sidebar">
    <section class="panel">
      <h3>FEATURED</h3>
      <ul><li>Cheeses (4)</li><li>Cured Meats (6)</li><li>Deli Spreads (5)</li><li>Fresh Bread (3)</li><li>Fruit (12)</li><li>Herbs (7)</li><li>Nuts &amp; Seeds (4)</li><li>Oils &amp; Vinegars (5)</li><li>Olives &amp; Antipasto (3)</li><li>Vegetables (14)</li></ul>
    </section>
    <section class="panel">
      <h3>SPECIALS</h3>
      <ul><li>Cheeses (2)</li><li>Cured Meats (3)</li><li>Deli Spreads (2)</li><li>Fresh Bread (1)</li><li>Fruit (5)</li><li>Herbs (2)</li><li>Nuts &amp; Seeds (1)</li><li>Vegetables (6)</li></ul>
    </section>
    <div class="promo">
      <div class="promo-photo" role="img" aria-label="Shopper choosing fresh fruit and vegetables at a produce stand"></div>
      <div class="promo-copy">
        <div><span class="fresh">FRESH</span><span class="quality">QUALITY</span></div>
        <div class="ready">FOOD READY TO BE</div>
        <div class="delivered">DELIVERED</div>
        <p>Hand picked produce and fine deli goods delivered to your door each morning.</p>
      </div>
    </div>
    <div class="newsletter">
      <h4>NEWSLETTER SIGNUP</h4>
      <p>Get our latest specials and seasonal news straight to your inbox.</p>
      <div class="field">Enter your email</div>
      <div class="btn">SUBSCRIBE NOW</div>
    </div>
  </aside>

  <main class="main">
    <section class="hero">
      <div class="hero-photo" role="img" aria-label="Smiling woman holding a paper bag full of fresh vegetables"></div>
      <div class="hero-copy">
        <h1>DAILY<br>DELIVERIES</h1>
        <p>Fresh deli goods and seasonal produce, picked and packed each morning and brought straight to your kitchen.</p>
        <span class="btn">SHOP ONLINE</span>
      </div>
    </section>

    <section class="features">
      <div class="feature">
        <span class="icon"><svg width="20" height="20" viewBox="0 0 24 24"><path fill="#fff" d="M12 3l9 8h-3v9h-5v-6h-2v6H6v-9H3z"/></svg></span>
        <div><h5>HOME DELIVERY</h5><p>Right to your door, across the city every day.</p></div>
      </div>
      <div class="feature">
        <span class="icon"><svg width="20" height="20" viewBox="0 0 24 24"><circle cx="12" cy="12" r="9" fill="none" stroke="#fff" stroke-width="2"/><path d="M12 7v5l3 3" stroke="#fff" stroke-width="2" fill="none"/></svg></span>
        <div><h5>DELIVERY ON TIME</h5><p>Choose your slot and we arrive right on time.</p></div>
      </div>
      <div class="feature">
        <span class="icon"><svg width="20" height="20" viewBox="0 0 24 24"><path d="M5 12.5l4.5 4.5L19 7" stroke="#fff" stroke-width="2.6" fill="none"/></svg></span>
        <div><h5>100% SATISFIED</h5><p>Not happy with an item? We replace it free.</p></div>
      </div>
    </section>

    <h2 class="section-title">PRODUCTS OF THE MONTH</h2>
    <div class="grid">
      <div class="card"><div class="thumb banana" role="img" aria-label="Bunch of bananas"></div><h6>Bananas 1kg</h6><div class="price"><s>$4.00</s>$3.00</div><div class="buy"><span class="qty">1</span><span class="btn">BUY NOW</span></div></div>
      <div class="card"><div class="thumb onion" role="img" aria-label="Brown onions"></div><h6>Brown Onions 1kg</h6><div class="price"><s>$4.00</s>$3.00</div><div class="buy"><span class="qty">1</span><span class="btn">BUY NOW</span></div></div>
      <div class="card"><div class="thumb chilli" role="img" aria-label="Red chillies"></div><h6>Chilli Lime 1kg</h6><div class="price"><s>$4.00</s>$3.00</div><div class="buy"><span class="qty">1</span><span class="btn">BUY NOW</span></div></div>
      <div class="card"><div class="thumb berry" role="img" aria-label="Strawberries"></div><h6>Bananas 1kg</h6><div class="price"><s>$4.00</s>$3.00</div><div class="buy"><span class="qty">1</span><span class="btn">BUY NOW</span></div></div>
      <div class="card"><div class="thumb orange" role="img" aria-label="Orange"></div><h6>Bananas 1kg</h6><div class="price"><s>$4.00</s>$3.00</div><div class="buy"><span class="qty">1</span><span class="btn">BUY NOW</span></div></div>
      <div class="card"><div class="thumb tomato" role="img" aria-label="Ripe tomatoes"></div><h6>Brown Onions 1kg</h6><div class="price"><s>$4.00</s>$3.00</div><div class="buy"><span class="qty">1</span><span class="btn">BUY NOW</span></div></div>
      <div class="card"><div class="thumb cabbage" role="img" aria-label="Green cabbage"></div><h6>Chilli Lime 1kg</h6><div class="price"><s>$4.00</s>$3.00</div><div class="buy"><span class="qty">1</span><span class="btn">BUY NOW</span></div></div>
      <div class="card"><div class="thumb fig" role="img" aria-label="Fresh figs"></div><h6>Bananas 1kg</h6><div class="price"><s>$4.00</s>$3.00</div><div class="buy"><span class="qty">1</span><span class="btn">BUY NOW</span></div></div>
    </div>

    <h2 class="section-title">SPECIALS PRODUCTS</h2>
    <div class="grid">
      <div class="card"><div class="thumb cherry" role="img" aria-label="Cherries"></div><h6>Bananas 1kg</h6><div class="price"><s>$4.00</s>$3.00</div><div class="buy"><span class="qty">1</span><span class="btn">BUY NOW</span></div></div>
      <div class="card"><div class="thumb pomegranate" role="img" aria-label="Pomegranates"></div><h6>Brown Onions 1kg</h6><div class="price"><s>$4.00</s>$3.00</div><div class="buy"><span class="qty">1</span><span class="btn">BUY NOW</span></div></div>
      <div class="card"><div class="thumb redonion" role="img" aria-label="Red onions"></div><h6>Chilli Lime 1kg</h6><div class="price"><s>$4.00</s>$3.00</div><div class="buy"><span class="qty">1</span><span class="btn">BUY NOW</span></div></div>
      <div class="card"><div class="thumb garlic" role="img" aria-label="Garlic bulbs"></div><h6>Bananas 1kg</h6><div class="price"><s>$4.00</s>$3.00</div><div class="buy"><span class="qty">1</span><span class="btn">BUY NOW</span></div></div>
    </div>
  </main>
</div>

<footer class="footer">
  <div class="wrap">
    <div class="col"><h6>WELCOME</h6><ul><li>Home</li><li>About Us</li><li>Delivery</li><li>Specials</li><li>Contact Us</li></ul></div>
    <div class="col"><h6>FEATURED PRODUCTS</h6><ul><li>Cheeses (4)</li><li>Cured Meats (6)</li><li>Deli Spreads (5)</li><li>Fresh Bread (3)</li><li>Fruit (12)</li></ul></div>
    <div class="col"><h6>&nbsp;</h6><ul><li>Herbs (7)</li><li>Nuts &amp; Seeds (4)</li><li>Oils (5)</li><li>Olives (3)</li><li>Vegetables (14)</li></ul></div>
    <div class="col"><h6>MY ACCOUNT</h6><ul><li>My Account</li><li>Order History</li><li>Wish List</li><li>Login</li><li>Register</li></ul></div>
    <div class="col"><h6>INFORMATION</h6><ul><li>Terms &amp; Conditions</li><li>Privacy Policy</li><li>Delivery Areas</li><li>Site Map</li></ul></div>
    <div class="col social"><h6>FOLLOW US</h6><ul><li><i></i>Community</li><li><i></i>Updates</li><li><i></i>Photos</li><li><i></i>Recipes</li></ul></div>
  </div>
  <div class="copyright">Copyright © 2024 pantryloop.com.au. All Rights Reserved.</div>
</footer>

</body>
</html>
```